PowerPoint Design Project

We need a powerpoint design for our consulting company, Halvern Consulting. We provide technology strategy and solutioning services, with an emphasis on cloud technology. More information about our services can be found at www.halvernconsulting-example.com

We are looking for a design that is professional, but not corporate stuffy. The design needs to use our primary colors in our brand.
Updates

Reason: We need to iterate on some of the great designs, plus, many people have not had a chance to submit their design yet.

Reason: We had a lot of people accept the project, but not all of them have responded yet. We wanted to get them some time, plus, ask a couple of people to make some minor revisions.

Target Market(s)

Technology buyers between the ages of 30-55 at Pinnacle 900 companies

Industry/Entity Type

It Company

Requirements
Must have
• Must follow our logo colors.
Must have at least a cover slide and interior content slide.
Should not have
• Should not contain anything cartoonish or anything with lots of clouds

```html
<!DOCTYPE html>
<html lang="en">
<head>
<meta charset="utf-8">
<title>Halvern Consulting — Content Slide</title>
<link href="https://fonts.googleapis.com/css2?family=Arimo:wght@400;700&display=swap" rel="stylesheet">
<style>
  :root {
    --bg-light: #fbfbfb;
    --bg-mid: #f0f0f0;
    --bg-dark: #e4e3e2;
    --brand-taupe: #7a6a5c;
    --text-teal: #3f7d80;
    --page-box: #cbc6c1;
    --page-text: #6e6155;
    --footer-text: #c2b6aa;
  }
  * { margin: 0; padding: 0; box-sizing: border-box; }
  html, body { width: 1200px; height: 900px; overflow: hidden; }
  body { font-family: "Arimo", Arial, sans-serif; }
  .slide { position: relative; width: 1200px; height: 900px; overflow: hidden; }
  .backdrop {
    position: absolute; inset: 0;
    background: linear-gradient(135deg, var(--bg-light) 0%, var(--bg-mid) 45%, var(--bg-dark) 100%);
  }
  .slide-title {
    position: absolute; left: 64px; top: 45px;
    font-size: 33px; font-weight: 700; color: var(--brand-taupe); letter-spacing: 0.3px;
  }
  .brand {
    position: absolute; right: 28px; top: 40px;
    font-size: 34px; font-weight: 400; color: var(--brand-taupe); letter-spacing: -0.5px;
  }
  .title-rule { position: absolute; left: 0; top: 93px; width: 1200px; height: 3px; background: var(--brand-taupe); }
  .point { position: absolute; left: 113px; width: 995px; font-size: 25px; line-height: 37px; color: var(--text-teal); }
  .point-icon { position: absolute; left: -57px; top: 2px; width: 34px; height: 34px; }
  .sub-point { position: absolute; left: 174px; width: 960px; font-size: 21.8px; line-height: 26px; color: var(--text-teal); white-space: nowrap; }
  .sub-icon { position: absolute; left: -27px; top: 6px; width: 14px; height: 14px; }
  .page-number {
    position: absolute; left: 1127px; top: 813px; width: 46px; height: 47px;
    background: var(--page-box); color: var(--page-text);
    font-size: 20px; font-weight: 700; display: flex; align-items: center; justify-content: center;
  }
  .footer {
    position: absolute; left: 0; top: 871px; width: 1200px; height: 29px;
    background: var(--brand-taupe); color: var(--footer-text);
    font-size: 16.8px; font-weight: 700; text-align: center; line-height: 31px;
  }
</style>
</head>
<body>
<div class="slide">
  <div class="backdrop" role="img" aria-label="Light grey background with a scattered pattern of faint square tiles"></div>

  <h1 class="slide-title">PROJECT TITLE</h1>
  <div class="brand">Halvern Consulting</div>
  <div class="title-rule"></div>

  <div class="point" style="top:150px">
    <svg class="point-icon" viewBox="0 0 34 34"><rect x="1.5" y="1.5" width="31" height="31" fill="none" stroke="#7a6a5c" stroke-width="3"/><path d="M11 9 L25 17 L11 25 Z" fill="#7a6a5c"/></svg>
    Lorem ipsum dolor sit amet lorem ipsum dolor sit amet lorem ipsum dolor sit amet lorem ipsum dolor sit amet
  </div>
  <div class="sub-point" style="top:244px"><svg class="sub-icon" viewBox="0 0 14 14"><path d="M0 0 L14 7 L0 14 Z" fill="#7a6a5c"/></svg>Lorem ipsum dolor sit amet lorem ipsum dolor sit amet lorem ipsum dolor sit amet lorem ipsum</div>
  <div class="sub-point" style="top:295px"><svg class="sub-icon" viewBox="0 0 14 14"><path d="M0 0 L14 7 L0 14 Z" fill="#7a6a5c"/></svg>Lorem ipsum dolor sit amet lorem ipsum dolor sit amet lorem ipsum dolor sit amet lorem ipsum</div>
  <div class="sub-point" style="top:348px"><svg class="sub-icon" viewBox="0 0 14 14"><path d="M0 0 L14 7 L0 14 Z" fill="#7a6a5c"/></svg>Lorem ipsum dolor sit amet lorem ipsum dolor sit amet lorem ipsum dolor sit amet lorem ipsum</div>

  <div class="point" style="top:411px">
    <svg class="point-icon" viewBox="0 0 34 34"><rect x="1.5" y="1.5" width="31" height="31" fill="none" stroke="#7a6a5c" stroke-width="3"/><path d="M11 9 L25 17 L11 25 Z" fill="#7a6a5c"/></svg>
    Lorem ipsum dolor sit amet lorem ipsum dolor sit amet lorem ipsum dolor sit amet lorem ipsum dolor sit amet lorem ipsum dolor sit amet lorem ipsum dolor sit amet lorem ipsum dolor sit amet lorem ipsum dolor sit amet lorem ipsum dolor sit amet lorem ipsum dolor sit amet lorem ipsum dolor sit amet lorem ipsum dolor sit amet
  </div>

  <div class="point" style="top:584px">
    <svg class="point-icon" viewBox="0 0 34 34"><rect x="1.5" y="1.5" width="31" height="31" fill="none" stroke="#7a6a5c" stroke-width="3"/><path d="M11 9 L25 17 L11 25 Z" fill="#7a6a5c"/></svg>
    Lorem ipsum dolor sit amet lorem ipsum dolor sit amet lorem ipsum dolor sit amet lorem ipsum dolor sit amet
  </div>
  <div class="sub-point" style="top:681px"><svg class="sub-icon" viewBox="0 0 14 14"><path d="M0 0 L14 7 L0 14 Z" fill="#7a6a5c"/></svg>Lorem ipsum dolor sit amet lorem ipsum dolor sit amet lorem ipsum dolor sit amet lorem ipsum</div>
  <div class="sub-point" style="top:732px"><svg class="sub-icon" viewBox="0 0 14 14"><path d="M0 0 L14 7 L0 14 Z" fill="#7a6a5c"/></svg>Lorem ipsum dolor sit amet lorem ipsum dolor sit amet lorem ipsum dolor sit amet lorem ipsum</div>

  <div class="page-number">01</div>
  <div class="footer">Copyright text here</div>
</div>
</body>
</html>
```